Create a Brochure Design for Thornbury Homecare

Thornbury Homecare is a subsidiary of the Thornbury Care Group. This brochure is specifically for the Thornbury Homecare company and brand. Create a 3 panel, A4, front and back, tri-fold brochure. This brochure will be a way to introduce our Homecare services to the community, prospective clients, and various referral partners. The brochure must be eye catching, unique in its deliverables and demonstrate both attention to detail and comfort. Our organization is sophisticated and built around warmth, care and individualized personal attention. The most important aspect of this design is to focus on creating a nurturing, warm, and inviting feel where you would want to have a Nurse or Nurse’s Aide in your own home or a loved one’s home.

I am open to the creativity of the designer to develop something based on the above criteria; however I would like the design to work well with the existing collateral material. What I mean by that is that while I want everything to have its own personality and stand out as its own brand representative, I still need to be able to tell that the overall design concept stays stylistically inside of the same ‘family’ of existing designed material. Because of this, below I would like for the designer to pull inspiration from the link to our website (Located below) as well as from the attachment of our recently refreshed business cards (Attached). This should allow each design to be unique and creative, while still staying inside of a framework and the feel/style that I am looking for.

Finally, I want all the designers to understand that this brochure design is for a private, in home, healthcare company where we are responsible for providing personalized care for a culturally and ethnically diverse make-up clientele of all ages. The photos that are used must represent an image of warmth, care, and a positive interaction between client and caregiver.

Look under the Thornbury Homecare tab at www.thornburycaregroup-example.net
Updates

Industry/Entity Type

Healthcare

Requirements
Must have
• • The Thornbury Homecare company logo must be included.

```html
<!DOCTYPE html>
<html lang="en">
<head>
<meta charset="utf-8">
<title>Thornbury Homecare – Tri-fold Brochure</title>
<link rel="stylesheet" href="https://fonts.googleapis.com/css2?family=Ubuntu:ital,wght@0,300;0,400;0,500;0,700;1,400&family=Dancing+Script:wght@500&display=swap">
<style>
:root{
  --teal-dark:#2a7472;
  --teal-mid:#5f9896;
  --teal-brand:#1f7a6c;
  --coral:#f4907a;
  --coral-soft:#f6a08c;
  --grey-dark:#6d6d6f;
  --grey-light:#d9d9da;
  --white:#ffffff;
  --ink:#444;
  --page:#ffffff;
}
*{box-sizing:border-box;margin:0;padding:0}
html,body{width:818px;height:1200px;overflow:hidden;background:var(--page)}
body{position:relative;font-family:"Ubuntu",sans-serif;color:var(--ink)}
.side-label{position:absolute;font-family:"Dancing Script",cursive;font-size:20px;color:#333}
.fold-label{position:absolute;font-family:"Dancing Script",cursive;font-size:12px;color:#333}
.fold-line{position:absolute;width:0;border-left:1px dashed #555}
.sheet{position:absolute;left:68px;width:688px;background:var(--white);box-shadow:0 3px 6px rgba(0,0,0,.25);overflow:hidden}
.sheet--exterior{top:78px;height:487px}
.sheet--interior{top:636px;height:486px}
.band{position:absolute;left:0;width:100%;height:19px;
  background:linear-gradient(90deg,var(--grey-dark) 0%,var(--grey-light) 20%,#8a8a8c 38%,var(--grey-light) 55%,#f3f3f3 68%,#8a8a8c 85%,var(--grey-dark) 100%)}
.band--top{top:0}
.band--bottom{bottom:0}
.band-wave{position:absolute;left:0;width:100%;height:30px}
.rule{position:absolute;left:0;width:100%;height:2px;background:var(--coral)}
.block{position:absolute}
.photo{position:absolute}
.brand-name{font-family:"Ubuntu",sans-serif;font-weight:400;color:var(--teal-brand);white-space:nowrap}
.brand-mark{display:inline-block;background:var(--coral);vertical-align:middle}
.tagline{font-style:italic;font-size:8px;letter-spacing:1.8px;line-height:11px}
/* exterior */
.contact{position:absolute;left:14px;top:114px;display:flex;align-items:center}
.contact-icon{width:50px;height:50px;border-radius:50%;background:#fff;box-shadow:0 1px 4px rgba(0,0,0,.3);display:flex;align-items:center;justify-content:center}
.contact-text{margin-left:11px}
.contact-kicker{font-size:6.5px;font-weight:700;color:var(--coral);letter-spacing:.2px}
.contact-phone{font-size:14px;font-weight:700;color:var(--coral)}
.facilities{position:absolute;left:0;top:160px;width:225px;height:310px;background:var(--teal-mid);padding:30px 0 0 40px;color:#fff}
.facilities h3{font-size:11px;font-weight:700;margin-bottom:12px}
.facilities li{list-style:none;font-size:7.6px;font-weight:300;height:21.3px}
.address-panel{position:absolute;left:225px;top:163px;width:232px;height:307px;background:var(--teal-dark);color:#fff;text-align:center;font-size:5.6px;letter-spacing:1px;line-height:7px;padding-top:177px}
.address-panel strong{font-weight:700}
.address-panel .divider{display:block;width:40px;height:1px;background:rgba(255,255,255,.7);margin:5px auto}
/* interior */
.feature{position:absolute;top:284px;width:230px;height:186px;padding:21px 24px 0 24px;color:#fff}
.feature h4{font-size:11px;font-weight:700;line-height:12.5px;margin-bottom:11px}
.feature .lead{font-size:7px;font-weight:700;line-height:10.4px;margin-bottom:9px;width:194px}
.feature .body{font-size:7px;font-weight:300;line-height:10.6px;opacity:.9;width:194px}
.badge{position:absolute;width:46px;height:46px;border-radius:50%;background:var(--coral-soft);color:#fff;font-size:6px;font-weight:500;text-align:center;display:flex;align-items:center;justify-content:center;line-height:8px}
</style>
</head>
<body>

<!-- EXTERIOR -->
<div class="side-label" style="left:68px;top:46px">exterior</div>
<div class="fold-label" style="left:297px;top:54px">fold</div>
<div class="fold-label" style="left:531px;top:54px">fold</div>

<section class="sheet sheet--exterior">
  <div class="band band--top"></div>
  <svg class="band-wave" style="top:6px" viewBox="0 0 688 30" preserveAspectRatio="none">
    <path d="M0 12 C150 18 300 22 420 18 C520 14 600 8 688 12 L688 30 L0 30 Z" fill="#fff"/>
    <path d="M0 12 C150 18 300 22 420 18 C520 14 600 8 688 12" stroke="var(--coral)" stroke-width="2" fill="none"/>
  </svg>

  <div class="contact">
    <div class="contact-icon">
      <svg width="26" height="26" viewBox="0 0 24 24"><path d="M6.6 2.5l3 3.6-1.8 2.4c1 2.2 2.9 4.3 5.4 5.6l2.3-1.8 3.6 2.9-1.6 3.6c-7.4.2-14-6.8-13.6-14z" fill="none" stroke="#bbb" stroke-width="1.3"/></svg>
    </div>
    <div class="contact-text">
      <div class="contact-kicker">CONTACT US TODAY</div>
      <div class="contact-phone">(555) 827-3190</div>
    </div>
  </div>

  <div class="block" style="left:225px;top:62px;width:232px;text-align:center">
    <div class="brand-name" style="font-size:12px;color:#555"><span class="brand-mark" style="width:9px;height:9px;background:#555;margin-right:5px"></span>Thornbury Care Group</div>
    <p class="tagline" style="color:#555;margin-top:12px">Caring you can count on...<br>Every single day.</p>
  </div>

  <div class="block" style="left:457px;top:70px;width:231px;text-align:center">
    <div class="brand-name" style="font-size:17px"><span class="brand-mark" style="width:14px;height:14px;margin-right:6px"></span>Thornbury Homecare</div>
  </div>

  <div class="rule" style="top:158px"></div>

  <div class="facilities">
    <h3>Modern Facilities</h3>
    <ul>
      <li>» PONDERUM PERICULIS</li>
      <li>» MODERATIUS AT PER</li>
      <li>» TE EOS MUNDI ACCUSAM</li>
      <li>» ADOLESCENS MEI</li>
      <li>» EX REQUE ELITR</li>
      <li>» EU INANI OPTION MEI</li>
      <li>» EI USU PAULO ANIMAL</li>
      <li>» SIGNIFERUMQUE</li>
      <li>» TEMPOR HENDRERIT ALIQUANDO</li>
      <li>» EA DUO, VIDIT DEMOCRITUM</li>
      <li>» MEI DIAM SEMPER TIMEAM IUS</li>
    </ul>
  </div>

  <div class="address-panel">
    <strong>Thornbury Homecare</strong><br>1480 Harbor View Rd., Suite 210<br>Lakemont, HI 96800
    <span class="divider"></span>
    <strong>Thornbury Senior Living</strong><br>42 Palm Grove Lane<br>Seacliff, HI 96701
    <span class="divider"></span>
    Phone: <strong>(555) 827-3190</strong><br>Fax: <strong>(555) 827-3195</strong><br>Email: <strong>info@thornburycare-example.com</strong><br>Website: <strong>www.thornburycare-example.com</strong>
  </div>

  <div class="photo" role="img" aria-label="Smiling nurse leaning beside a happy senior man" style="left:457px;top:162px;width:231px;height:308px;background:linear-gradient(120deg,#8a6a58 0%,#e8d8cc 35%,#d99a86 60%,#b8cde0 100%)"></div>

  <div class="band band--bottom"></div>
</section>

<!-- INTERIOR -->
<div class="side-label" style="left:68px;top:604px">interior</div>
<div class="fold-label" style="left:305px;top:612px">fold</div>
<div class="fold-label" style="left:540px;top:612px">fold</div>

<section class="sheet sheet--interior">
  <div class="band band--top"></div>
  <svg class="band-wave" style="top:6px" viewBox="0 0 688 30" preserveAspectRatio="none">
    <path d="M0 10 C150 16 300 20 420 17 C520 14 600 8 688 12 L688 30 L0 30 Z" fill="#fff"/>
    <path d="M0 10 C150 16 300 20 420 17 C520 14 600 8 688 12" stroke="var(--coral)" stroke-width="2" fill="none"/>
  </svg>

  <div class="block" style="left:0;top:48px;width:230px;text-align:center">
    <div class="brand-name" style="font-size:14px"><span class="brand-mark" style="width:12px;height:12px;margin-right:5px"></span>Thornbury Homecare</div>
  </div>
  <p class="tagline block" style="left:518px;top:66px;color:var(--teal-dark);font-size:7px">Caring you can count on...<br>Every single day.</p>

  <div class="rule" style="top:114px"></div>

  <div class="photo" role="img" aria-label="Senior man smiling with his caregiver" style="left:0;top:118px;width:230px;height:143px;background:linear-gradient(100deg,#b9a79a 0%,#e6dcd3 45%,#f1e9e2 100%)"></div>
  <div class="photo" role="img" aria-label="Caregiver holding an elderly person's hands" style="left:230px;top:118px;width:230px;height:143px;background:linear-gradient(110deg,#e8e4ea 0%,#d8b8a8 45%,#c79e8c 60%,#e9e4ea 100%)"></div>
  <div class="photo" role="img" aria-label="Nurse chatting with a smiling senior woman" style="left:460px;top:118px;width:228px;height:143px;background:linear-gradient(100deg,#3c4a6e 0%,#c9b4a4 45%,#9aa7c4 75%,#c0a688 100%)"></div>

  <div class="badge" style="left:172px;top:216px">Xxxxx<br>Xxxxxxxx</div>
  <div class="badge" style="left:411px;top:226px">Xxxxx<br>Xxxxxxxx</div>
  <div class="badge" style="left:638px;top:226px">Xxxxx<br>Xxxxxxxx</div>

  <div class="feature" style="left:0;background:var(--teal-dark)">
    <h4>Lorem ipsum dolor sit amet<br>at nostrum definitiones</h4>
    <p class="lead">Ponderum periculis moderatius at per. Te eos mundi accusam adolescens, mei ex reque elitr, eu inani option mei. Ei usu paulo animal signifer­umque. Tempor hendrerit aliquando ea duo, vidit democritum mei te, id diam semper timeam ius.</p>
    <p class="body">Rebum illud facilis in nam, ius recteque dissentiunt cu, antiopam splendide abhorreant et mel. Per et populo minimum.</p>
  </div>
  <div class="feature" style="left:230px;background:var(--teal-mid)">
    <h4>Lorem ipsum dolor sit amet<br>at nostrum definitiones</h4>
    <p class="lead">Ponderum periculis moderatius at per. Te eos mundi accusam adolescens, mei ex reque elitr, eu inani option mei. Ei usu paulo animal signifer­umque. Tempor hendrerit aliquando ea duo, vidit democritum mei te, id diam semper timeam ius.</p>
    <p class="body">Rebum illud facilis in nam, ius recteque dissentiunt cu, antiopam splendide abhorreant et mel. Per et populo minimum.</p>
  </div>
  <div class="feature" style="left:460px;width:228px;background:var(--teal-dark)">
    <h4>Lorem ipsum dolor sit amet<br>at nostrum definitiones</h4>
    <p class="lead">Ponderum periculis moderatius at per. Te eos mundi accusam adolescens, mei ex reque elitr, eu inani option mei. Ei usu paulo animal signifer­umque. Tempor hendrerit aliquando ea duo, vidit democritum mei te, id diam semper timeam ius.</p>
    <p class="body">Rebum illud facilis in nam, ius recteque dissentiunt cu, antiopam splendide abhorreant et mel. Per et populo minimum.</p>
  </div>

  <div class="band band--bottom"></div>
</section>

<div class="fold-line" style="left:293px;top:52px;height:534px"></div>
<div class="fold-line" style="left:525px;top:52px;height:534px"></div>
<div class="fold-line" style="left:299px;top:610px;height:536px"></div>
<div class="fold-line" style="left:532px;top:610px;height:536px"></div>

</body>
</html>
```